Adult Store requires exciting banner ad designs for online store

Coral Haze requires an online estore homepage design template for slider ads, banner ads designs, collection ad designs, product specific ad design - based on current brand theme featuring sexy fun inked up girls & and guys and build on the australia bondi beach location.
Our current tagline is 'Time For A New Vibe?'
The ad design specs should be based on normal website design specs
www.coralhaze.example

Target Market(s)

Women and men 18-35 shopping online for a new adult toys
Shoppers looking for something different in the category
Pregnant females looking for sex toys

Font styles to use
Sans Serif

Colors

Designer to choose colors to be used in the design.

Requirements
Must have
• * Build on the worldwide popularity of the Bondi beach location
• Must include company logo with tag line
• * Must include website address
• * Sex Toys Factory outlet clearance Sale or Sex toys clearance sale
• * WORLDWIDE SAME DAY SHIPPING x 7-Days (or your variation)
• * Include inked up girl image or guru
• * Has a call to action (Click me etc)
• * Attention grabbing, fun & exciting yet still professional
• * Include tasteful images that shoppers want to be like
• * Promotes only a visitor who is interested to click
• * Include somewhere 'Proudly Australian Owned & Operated logo'
• * Include reference to hens / bucks parties
• * Looking for your own creative flair, be original !!
Nice to have
• Subtle inked up tattoo theme, images of sexy young seductive inked up girls and guys, gay and straight.
Should not have
• Images or text deemed offensive
• Ads and background should not have overly Dark repressive colours

```html
<!DOCTYPE html>
<html lang="en">
<head>
<meta charset="utf-8">
<title>Coral Haze – Banner Ad Set</title>
<link rel="stylesheet" href="https://fonts.googleapis.com/css2?family=Bebas+Neue&family=Montserrat:wght@400;500;600;700&display=swap">
<style>
:root{
  --blue:#0a6fc9;
  --blue-line:#2a82d4;
  --magenta:#c51fe0;
  --magenta-dark:#9c12c0;
  --dark:#2e2a2b;
  --white:#ffffff;
  --label:#3a3a3a;
  --border:#c9c9c9;
  --photo-light:#efe3dc;
  --photo-mid:#c98a72;
  --photo-deep:#8a3424;
}
*{box-sizing:border-box;margin:0;padding:0}
html,body{width:1200px;height:1200px;overflow:hidden;background:var(--white)}
body{position:relative;font-family:"Montserrat",Arial,sans-serif}

.size-label{position:absolute;font-size:17px;font-weight:500;color:var(--label);transform:translateX(-50%);white-space:nowrap;letter-spacing:.2px}

.banner{position:absolute;overflow:hidden;background:var(--white);border:1px solid var(--border)}
.banner > *{position:absolute}

.header{background:var(--white)}
.panel{background:var(--blue)}
.photo{background:linear-gradient(160deg,var(--photo-light) 0%,var(--photo-mid) 45%,var(--photo-deep) 100%)}
.shipping{background:var(--dark);color:var(--white);font-weight:700;text-align:center;display:flex;align-items:center;justify-content:center;line-height:1.25;letter-spacing:.3px}

.brand{display:flex;align-items:center;gap:6px}
.brand-dot{width:26px;height:26px;border-radius:50%;background:var(--magenta);flex:none}
.brand-text{display:flex;flex-direction:column;line-height:1}
.brand-name{font-weight:700;font-size:21px;color:var(--blue)}
.brand-url{font-size:10.5px;color:var(--magenta);margin-top:3px}

.badge{border-radius:50%;background:var(--white);border:5px solid var(--blue)}
.badge::after{content:"";position:absolute;inset:18%;border-radius:50%;background:var(--dark)}

.headline{font-family:"Bebas Neue",Impact,sans-serif;color:var(--white);line-height:1;white-space:nowrap}
.subline{color:var(--white);font-weight:500;line-height:1.2}
.cta{border-radius:999px;background:linear-gradient(var(--magenta),var(--magenta-dark));color:var(--white);font-weight:600;display:flex;align-items:center;justify-content:center;box-shadow:0 2px 3px rgba(0,0,0,.25);letter-spacing:.3px}
</style>
</head>
<body>

<div class="size-label" style="left:296px;top:127px">Medium Rectangle 300 x 250</div>
<div class="size-label" style="left:577px;top:127px">Skyscraper 160 x 600</div>
<div class="size-label" style="left:919px;top:127px">Largest Rectangle 425 x 600</div>
<div class="size-label" style="left:296px;top:477px">Square 250 x 250</div>
<div class="size-label" style="left:511px;top:847px">Leaderboard 728 x 90</div>

<!-- Medium Rectangle -->
<section class="banner" style="left:147px;top:170px;width:300px;height:250px">
  <div class="panel" style="left:0;top:62px;width:300px;height:158px"></div>
  <div class="header" style="left:0;top:0;width:190px;height:62px"></div>
  <div class="photo" role="img" aria-label="Photo of a tattooed red-haired woman playfully poking out her tongue" style="left:190px;top:0;width:110px;height:220px"></div>
  <div class="brand" style="left:8px;top:12px"><span class="brand-dot"></span><span class="brand-text"><span class="brand-name">Coral Haze</span><span class="brand-url">www.coralhaze.example</span></span></div>
  <div class="badge" role="img" aria-label="Australian owned and operated badge" style="left:136px;top:72px;width:76px;height:76px"></div>
  <div class="headline" style="left:14px;top:92px;font-size:40px">SEX TOYS</div>
  <div class="subline" style="left:16px;top:131px;font-size:15.5px">Factory outlet<br>clearance Sale</div>
  <div class="cta" style="left:9px;top:175px;width:120px;height:30px;font-size:13px">LEARN MORE</div>
  <div class="shipping" style="left:0;top:220px;width:300px;height:30px;font-size:11.5px">WORLDWIDE SAME DAY SHIPPING X 7-DAYS</div>
</section>

<!-- Square -->
<section class="banner" style="left:147px;top:520px;width:250px;height:250px">
  <div class="panel" style="left:0;top:56px;width:250px;height:150px"></div>
  <div class="header" style="left:0;top:0;width:155px;height:56px"></div>
  <div class="photo" role="img" aria-label="Photo of a tattooed red-haired woman playfully poking out her tongue" style="left:155px;top:0;width:95px;height:206px"></div>
  <div class="brand" style="left:6px;top:12px"><span class="brand-dot" style="width:22px;height:22px"></span><span class="brand-text"><span class="brand-name" style="font-size:18px">Coral Haze</span><span class="brand-url" style="font-size:9.5px">www.coralhaze.example</span></span></div>
  <div class="badge" role="img" aria-label="Australian owned and operated badge" style="left:127px;top:63px;width:74px;height:74px"></div>
  <div class="headline" style="left:7px;top:84px;font-size:38px">SEX TOYS</div>
  <div class="subline" style="left:9px;top:121px;font-size:15px">Factory outlet<br>clearance Sale</div>
  <div class="cta" style="left:7px;top:165px;width:121px;height:30px;font-size:12.5px">LEARN MORE</div>
  <div class="shipping" style="left:0;top:206px;width:250px;height:44px;font-size:11.5px">WORLDWIDE SAME DAY<br>SHIPPING X 7-DAYS</div>
</section>

<!-- Skyscraper -->
<section class="banner" style="left:497px;top:170px;width:160px;height:600px">
  <div class="header" style="left:0;top:0;width:160px;height:61px"></div>
  <div class="brand" style="left:5px;top:14px;gap:4px"><span class="brand-dot" style="width:20px;height:20px"></span><span class="brand-text"><span class="brand-name" style="font-size:17px">Coral Haze</span><span class="brand-url" style="font-size:9px">www.coralhaze.example</span></span></div>
  <div class="photo" role="img" aria-label="Photo of a tattooed red-haired woman playfully poking out her tongue" style="left:0;top:61px;width:160px;height:225px"></div>
  <div class="panel" style="left:0;top:286px;width:160px;height:235px"></div>
  <div class="badge" role="img" aria-label="Australian owned and operated badge" style="left:34px;top:259px;width:90px;height:90px"></div>
  <div class="headline" style="left:0;width:160px;text-align:center;top:362px;font-size:44px">SEX TOYS</div>
  <div class="subline" style="left:0;width:160px;text-align:center;top:406px;font-size:17.5px">Factory outlet<br>clearance Sale</div>
  <div class="cta" style="left:8px;top:460px;width:144px;height:35px;font-size:15px">LEARN MORE</div>
  <div class="shipping" style="left:0;top:521px;width:160px;height:79px;font-size:11.5px">WORLDWIDE<br>SAME DAY SHIPPING<br>X 7-DAYS</div>
</section>

<!-- Largest Rectangle -->
<section class="banner" style="left:707px;top:170px;width:425px;height:600px">
  <div class="header" style="left:0;top:0;width:425px;height:61px;border-bottom:2px solid #e4e4e4"></div>
  <div class="brand" style="left:132px;top:13px"><span class="brand-dot"></span><span class="brand-text"><span class="brand-name">Coral Haze</span><span class="brand-url">www.coralhaze.example</span></span></div>
  <div class="photo" role="img" aria-label="Photo of a tattooed red-haired woman playfully poking out her tongue, tattooed arm at right" style="left:0;top:63px;width:425px;height:307px;background:linear-gradient(90deg,var(--white) 0%,var(--photo-mid) 25%,var(--photo-deep) 50%,var(--photo-mid) 75%,var(--white) 100%)"></div>
  <div class="panel" style="left:0;top:370px;width:425px;height:200px"></div>
  <div class="badge" role="img" aria-label="Australian owned and operated badge" style="left:153px;top:280px;width:118px;height:118px;border-width:6px"></div>
  <div class="headline" style="left:0;width:425px;text-align:center;top:407px;font-size:54px">SEX TOYS</div>
  <div class="subline" style="left:0;width:425px;text-align:center;top:463px;font-size:21px">Factory outlet clearance Sale</div>
  <div class="cta" style="left:124px;top:507px;width:180px;height:43px;font-size:19px">LEARN MORE</div>
  <div class="shipping" style="left:0;top:570px;width:425px;height:30px;font-size:12px">WORLDWIDE SAME DAY SHIPPING X 7-DAYS</div>
</section>

<!-- Leaderboard -->
<section class="banner" style="left:147px;top:890px;width:728px;height:90px">
  <div class="header" style="left:0;top:0;width:172px;height:90px"></div>
  <div class="brand" style="left:8px;top:27px"><span class="brand-dot"></span><span class="brand-text"><span class="brand-name">Coral Haze</span><span class="brand-url">www.coralhaze.example</span></span></div>
  <div class="photo" role="img" aria-label="Photo of a tattooed red-haired woman playfully poking out her tongue" style="left:172px;top:0;width:84px;height:90px"></div>
  <div class="panel" style="left:256px;top:0;width:322px;height:90px"></div>
  <div class="badge" role="img" aria-label="Australian owned and operated badge" style="left:249px;top:7px;width:76px;height:76px"></div>
  <div class="headline" style="left:331px;top:9px;font-size:38px">SEX TOYS</div>
  <div class="subline" style="left:453px;top:8px;font-size:15px">Factory outlet<br>clearance Sale</div>
  <div class="cta" style="left:386px;top:51px;width:120px;height:29px;font-size:12.5px">LEARN MORE</div>
  <div class="shipping" style="left:578px;top:0;width:150px;height:90px;font-size:11.5px;line-height:1.55">WORLDWIDE SAME<br>DAY SHIPPING<br>X 7-DAYS</div>
</section>

</body>
</html>
```